Website for Corvalind Capital, my new firm that raises money from investors to buy, build, own an...

Corvalind Capital needs a website! We are a new company with very experienced people, who invest in, own and build hotel properties, as well as apartments and other commercial real estate. We seek investors for our projects, and we provide safe, secure returns on their investment in our projects. Our new logo is designed to exhibit strength, class and security, and would like our website to continue on this theme. Our name, Corvalind, is a word-play on a Greek word “aristeia”, which means “excellence” and “a warriors finest moment of glory in war”. If you are in business, you realize that much of it is like war, with strategy and moves and opponents and competitors, and ever-changing economic conditions and threats that make business very much like war. We like to think that we are good at business (war), and so have named our company “Corvalind”, using the founders last name and the word “aristeia” combined. Another definition of "aristeia" is "performing at the peak of one's potential after a long struggle"...again, much like business in real life! The website design should exhibit financial security, smart moves, and positive growth towards a bright future.

Target Market(s)

The target market is smart and wealthy investors, with others such as brokers, cities and government agencies, lenders, sellers, partners, etc also looking at it.

Industry/Entity Type

Investment

Number of Pages Required

5+ page

Font styles to use
Sans Serif

Colors
fec214

Requirements
Must have
• Our website should have a landing page, a "about" or bio page, a projects page and a contact us page. Our new logo uses the colors black and gold, so this should be factored in to our site. The site should be simple, yet impactful and impressive. I have actually two logos, which can be mixed and interchanged in a complimentary way, each with their own unique look.
Nice to have
• I have uploaded a couple screenshots of a website i like, and the simplicity I mention.
Should not have
• The site should not be flashy or complicated or complex or "busy"

```html
<!DOCTYPE html>
<html lang="en">
<head>
<meta charset="utf-8">
<title>Corvalind Capital — Projects</title>
<link href="https://fonts.googleapis.com/css2?family=Open+Sans:wght@400;500;600;700&family=Josefin+Sans:wght@400&display=swap" rel="stylesheet">
<style>
  :root {
    --bg-light: #f6f3e8;
    --bg-mid: #e6e0cc;
    --bg-dark: #c9c3ae;
    --panel: rgba(252, 251, 248, 0.95);
    --gold: #b8923a;
    --ink: #111111;
    --heading: #333333;
    --white: #ffffff;
  }
  * { margin: 0; padding: 0; box-sizing: border-box; }
  html, body { width: 1200px; height: 966px; overflow: hidden; }
  body {
    position: relative;
    font-family: "Open Sans", sans-serif;
    color: var(--ink);
    background:
      radial-gradient(ellipse at 50% 5%, #fbf9ef 0%, transparent 55%),
      linear-gradient(135deg, var(--bg-mid) 0%, var(--bg-light) 35%, var(--bg-mid) 65%, var(--bg-dark) 100%);
  }
  .brand {
    position: absolute; left: 50px; top: 55px;
    font-family: "Josefin Sans", sans-serif;
    font-size: 25px; letter-spacing: 1px;
    text-transform: uppercase; color: var(--ink);
  }
  .main-nav { position: absolute; top: 22px; left: 800px; display: flex; gap: 6px; }
  .main-nav a {
    display: block; padding: 4px 10px; height: 25px;
    font-size: 13.5px; line-height: 17px; text-transform: uppercase;
    color: var(--white); text-decoration: none; border-radius: 13px;
  }
  .main-nav a.active { background: var(--gold); }
  .content-panel {
    position: absolute; left: 62px; top: 148px; width: 1076px; height: 840px;
    background: var(--panel); border-radius: 10px;
  }
  .page-title {
    position: absolute; left: 0; top: 78px; width: 163px; text-align: right;
    font-size: 37px; font-weight: 700; letter-spacing: -1.5px; color: var(--heading);
  }
  .divider { position: absolute; left: 189px; top: 69px; width: 2.5px; height: 800px; background: var(--ink); }
  .project { position: absolute; width: 403px; }
  .project-image { position: relative; height: 182px; }
  .project-tag {
    position: absolute; right: 0; bottom: -12px;
    padding: 0 9px; height: 24px; line-height: 24px;
    font-size: 13.5px; font-weight: 500; color: var(--white);
    background: var(--gold); border-radius: 12px;
  }
  .project-text { margin: 30px 0 0 28px; width: 355px; font-size: 13.3px; line-height: 18.3px; font-weight: 500; }
  .apartments .project-image {
    background:
      radial-gradient(ellipse at 55% 70%, rgba(236,230,220,0.95) 0%, rgba(214,205,190,0.6) 35%, transparent 65%),
      linear-gradient(160deg, #7fbde6 0%, #b9d6ec 40%, #8ea4c4 75%, #d7b88f 100%);
  }
  .hotels .project-image {
    background:
      radial-gradient(ellipse at 50% 65%, rgba(226,180,150,0.55) 0%, transparent 60%),
      linear-gradient(180deg, #b9b8dc 0%, #8c7f95 30%, #6a5655 60%, #3f3a4a 100%);
  }
  .offices .project-image {
    background:
      radial-gradient(ellipse at 45% 60%, rgba(240,220,170,0.45) 0%, transparent 45%),
      linear-gradient(180deg, #aab0da 0%, #6f77a3 40%, #3f4566 75%, #1f2435 100%);
  }
  .resorts .project-image {
    background:
      radial-gradient(ellipse at 72% 85%, rgba(226,212,190,0.95) 0%, rgba(180,165,145,0.6) 35%, transparent 60%),
      linear-gradient(180deg, #0f63cc 0%, #2f7fd8 45%, #6aa3de 75%, #b9ada0 100%);
  }
</style>
</head>
<body>
  <div class="brand">Corvalind Capital</div>
  <nav class="main-nav">
    <a href="#">Home</a>
    <a href="#">About</a>
    <a href="#" class="active">Projects</a>
    <a href="#">Contact</a>
  </nav>

  <main class="content-panel">
    <h1 class="page-title">projects</h1>
    <div class="divider"></div>

    <article class="project apartments" style="left:192px; top:69px;">
      <div class="project-image" role="img" aria-label="Photo of a modern white apartment building with balconies under a blue sky">
        <span class="project-tag">Apartments</span>
      </div>
      <p class="project-text">Lorem ipsum dolor sit amet, consectetur adipiscing elit. Aenean sed neque non urna tempor molestie. Nulla nunc velit, porta id ex non, ultricies lobortis nunc. Donec finibus dolor eu velit sollicitudin sagittis. Etiam et eros sed nibh mollis egestas nec eget erat. Suspendisse euismod tortor ipsum. Fusce eu congue sapien. Proin ac ipsum purus.</p>
    </article>

    <article class="project hotels" style="left:595px; top:69px;">
      <div class="project-image" role="img" aria-label="Photo of a hotel facade with lit glass balconies at dusk">
        <span class="project-tag">Hotels</span>
      </div>
      <p class="project-text">Lorem ipsum dolor sit amet, consectetur adipiscing elit. Aenean sed neque non urna tempor molestie. Nulla nunc velit, porta id ex non, ultricies lobortis nunc. Donec finibus dolor eu velit sollicitudin sagittis. Etiam et eros sed nibh mollis egestas nec eget erat. Suspendisse euismod tortor ipsum. Fusce eu congue sapien. Proin ac ipsum purus.</p>
    </article>

    <article class="project offices" style="left:192px; top:439px;">
      <div class="project-image" role="img" aria-label="Photo of a glass office building at twilight">
        <span class="project-tag">Offices</span>
      </div>
      <p class="project-text">Lorem ipsum dolor sit amet, consectetur adipiscing elit. Aenean sed neque non urna tempor molestie. Nulla nunc velit, porta id ex non, ultricies lobortis nunc. Donec finibus dolor eu velit sollicitudin sagittis. Etiam et eros sed nibh mollis egestas nec eget erat. Suspendisse euismod tortor ipsum. Fusce eu congue sapien. Proin ac ipsum purus.</p>
    </article>

    <article class="project resorts" style="left:595px; top:439px;">
      <div class="project-image" role="img" aria-label="Photo of a resort building with terraces under a bright blue sky">
        <span class="project-tag">Resorts</span>
      </div>
      <p class="project-text">Lorem ipsum dolor sit amet, consectetur adipiscing elit. Aenean sed neque non urna tempor molestie. Nulla nunc velit, porta id ex non, ultricies lobortis nunc. Donec finibus dolor eu velit sollicitudin sagittis. Etiam et eros sed nibh mollis egestas nec eget erat. Suspendisse euismod tortor ipsum. Fusce eu congue sapien. Proin ac ipsum purus.</p>
    </article>
  </main>
</body>
</html>
```